Corrowin Sack operates across the US and Australasia providing calico bags to small business through to large enterprise across all verticals. Our bags are the most premium in the market place and our customer service is second to none. Our competitive advantage lays in our competitive pricing, superior quality and outstanding customer service.

Industry/Entity Type

Business

Contact Information for Business Card

Corrowin Sack
Marisol Quenby
Managing Director
marisol@corrowinsack.com
www.corrowinsack.com.au
Mobile:- 0471 896 305
Level 3, 284 Harwick Street
Melbourne Victoria Australia 3000

```html
<!DOCTYPE html>
<html lang="en">
<head>
<meta charset="utf-8">
<title>Corrowin Sack — Business Card</title>
<link rel="stylesheet" href="https://fonts.googleapis.com/css2?family=Source+Sans+3:wght@400;600&display=swap">
<style>
  :root {
    --stage: #3f3f3f;
    --burlap: #cbc1ae;
    --burlap-deep: #b9ae99;
    --orange: #f25a22;
    --ink: #1d1b17;
    --seam: #d9cfbc;
    --white: #ffffff;
  }
  * { margin: 0; padding: 0; box-sizing: border-box; }
  html, body {
    width: 1105px;
    height: 1200px;
    overflow: hidden;
    background: var(--stage);
    font-family: "Source Sans 3", "Helvetica Neue", Arial, sans-serif;
  }
  .sheet {
    position: relative;
    width: 1105px;
    height: 1200px;
  }
  .card {
    position: absolute;
    left: 192px;
    width: 721px;
    height: 411px;
    overflow: hidden;
    background: var(--burlap);
  }
  .card--front { top: 166px; }
  .card--back  { top: 622px; }
  .burlap {
    position: absolute;
    inset: 0;
    background: radial-gradient(ellipse at 40% 40%, var(--burlap) 0%, var(--burlap-deep) 100%);
  }
  .wave {
    position: absolute;
    inset: 0;
    width: 721px;
    height: 411px;
  }
  .brand {
    position: absolute;
    display: flex;
    align-items: center;
    gap: 10px;
    color: var(--orange);
    font-weight: 600;
    font-size: 30px;
    line-height: 1;
    white-space: nowrap;
  }
  .brand__dot {
    width: 22px;
    height: 22px;
    border-radius: 50%;
    background: var(--orange);
    flex: none;
  }
  .card--front .brand { left: 60px; top: 106px; }
  .card--back .brand  { left: 400px; top: 222px; }
  .contact {
    position: absolute;
    right: 37px;
    top: 168px;
    text-align: right;
    color: var(--white);
  }
  .contact__name {
    font-size: 26px;
    font-weight: 600;
    line-height: 30px;
  }
  .contact__role {
    font-size: 20px;
    font-weight: 400;
    line-height: 26px;
    margin-bottom: 16px;
  }
  .contact__address {
    font-size: 19px;
    line-height: 28px;
    margin-bottom: 6px;
  }
  .contact__line {
    display: flex;
    justify-content: flex-end;
    align-items: center;
    gap: 14px;
    font-size: 19px;
    line-height: 29px;
  }
  .contact__icon {
    width: 18px;
    height: 18px;
    flex: none;
  }
  .social {
    position: absolute;
    left: 511px;
    top: 344px;
    display: flex;
    gap: 14px;
  }
  .social__mark {
    width: 24px;
    height: 24px;
    border-radius: 50%;
    background: var(--orange);
  }
</style>
</head>
<body>
<main class="sheet">

  <section class="card card--front" aria-label="Business card front">
    <div class="burlap" role="img" aria-label="Natural burlap cotton texture"></div>
    <svg class="wave" viewBox="0 0 721 411" aria-hidden="true">
      <path d="M0,258 C90,318 190,350 275,343 C360,336 410,228 480,148 C540,83 620,56 721,58 L721,411 L0,411 Z" fill="var(--ink)"/>
      <path d="M0,300 C90,345 190,368 275,360 C360,352 415,240 485,160 C545,92 625,68 721,68 L721,411 L0,411 Z" fill="var(--orange)" stroke="var(--seam)" stroke-width="3"/>
    </svg>
    <div class="brand"><span class="brand__dot"></span>Corrowin Sack</div>
    <div class="contact">
      <p class="contact__name">Marisol Quenby</p>
      <p class="contact__role">Managing Director</p>
      <p class="contact__address">Level 3, 284 Harwick Street<br>Melbourne Victoria Australia 3000</p>
      <p class="contact__line">0471 896 305
        <svg class="contact__icon" viewBox="0 0 18 18" aria-hidden="true"><rect x="5" y="1" width="9" height="16" rx="1.5" fill="none" stroke="var(--white)" stroke-width="1.8"/><circle cx="9.5" cy="14" r="1" fill="var(--white)"/></svg>
      </p>
      <p class="contact__line">marisol@corrowinsack.com
        <svg class="contact__icon" viewBox="0 0 18 18" aria-hidden="true"><rect x="1" y="4" width="16" height="11" fill="var(--white)"/><path d="M1,4 L9,10 L17,4" fill="none" stroke="var(--orange)" stroke-width="1.4"/></svg>
      </p>
      <p class="contact__line">www.corrowinsack.com.au
        <svg class="contact__icon" viewBox="0 0 18 18" aria-hidden="true"><circle cx="9" cy="9" r="8" fill="var(--white)"/><path d="M5,5 C8,6 7,9 9,10 C10,12 8,14 9,16 M12,3 C11,6 14,7 15,6" fill="none" stroke="var(--orange)" stroke-width="1.5"/></svg>
      </p>
    </div>
  </section>

  <section class="card card--back" aria-label="Business card back">
    <div class="burlap" role="img" aria-label="Natural burlap cotton texture"></div>
    <div class="brand"><span class="brand__dot"></span>Corrowin Sack</div>
    <div class="social" aria-label="Social media">
      <span class="social__mark"></span>
      <span class="social__mark"></span>
      <span class="social__mark"></span>
    </div>
  </section>

</main>
</body>
</html>
```